Quiver Upcoming Gigs

One page graphic with my upcoming dates. Logo and photo attached, and sample from last flyer. Text:

QUIVER

UPCOMING DATES

3/26/18 Velvet Grotto (Las Vegas, NV)

4/1/18 Lantern Hall 2847 M St (Sac, CA)

4/8/18 Blue Heron (Sac, CA)

5/5/18 Open Lanes @ Silver Otter (Sac, CA)

5/10/18 Dunmore Fine Gallery (Sac, CA)

5/11/18 Bas Rive @ Cafe du Pont (Sac, CA)

5/27/18 Sunloft LBW @ Vox (Sac, CA)

Save The Date: 9/21/18 Moonweaver Festival (Puerto Nuevo, MX)

facebook.com/quiver530

Target Market(s)

House/Electronic Music

Industry/Entity Type

Night Club

Font styles to use
Sans Serif

Colors

Designer to choose colors to be used in the design.

Requirements
Must have
• Quiver logo or something that looks good instead. Prefer photo to be in but not necessary.
Nice to have

```html
<!DOCTYPE html>
<html lang="en">
<head>
<meta charset="utf-8">
<title>Quiver Upcoming Dates</title>
<link rel="stylesheet" href="https://fonts.googleapis.com/css2?family=Cinzel:wght@400&family=Roboto+Slab:wght@400;800&display=swap">
<style>
  :root {
    --navy-deep: #050a26;
    --navy: #0b1848;
    --royal: #1f35b8;
    --electric: #2a45e6;
    --gold: #e8c23c;
    --gold-soft: #b89232;
    --date-red: #e0201c;
    --text-light: #f1f1f4;
    --band: rgba(3, 6, 22, 0.78);
    --social-dot: #3b5bb0;
  }
  * { margin: 0; padding: 0; box-sizing: border-box; }
  html, body { width: 1200px; height: 660px; overflow: hidden; background: var(--navy-deep); }
  .poster {
    position: relative; width: 1200px; height: 660px; overflow: hidden;
    background:
      radial-gradient(ellipse at 20% 20%, rgba(42, 69, 230, 0.35), transparent 55%),
      linear-gradient(120deg, var(--navy-deep) 0%, var(--navy) 50%, var(--royal) 100%);
    font-family: "Roboto Slab", Georgia, serif;
  }
  .photo-area {
    position: absolute; top: 0; right: 0; width: 640px; height: 660px;
    clip-path: polygon(22% 0, 100% 0, 100% 100%, 0 100%, 8% 55%);
    background:
      radial-gradient(ellipse at 55% 45%, rgba(90, 110, 255, 0.55), transparent 60%),
      linear-gradient(160deg, #1a2a9e 0%, #2238d0 45%, #0c1660 100%);
  }
  .brand-name {
    position: absolute; left: 48px; top: 26px;
    font-family: "Roboto Slab", Georgia, serif;
    font-weight: 800; font-size: 124px; line-height: 1; letter-spacing: 2px;
    color: var(--gold);
  }
  .section-title {
    position: absolute; left: 53px;
    font-family: "Cinzel", Georgia, serif; font-weight: 400;
    color: var(--text-light); letter-spacing: 20px; line-height: 1;
  }
  .section-title.upcoming { top: 166px; font-size: 30px; }
  .section-title.save { top: 508px; font-size: 32px; letter-spacing: 19px; }
  .gold-rule {
    position: absolute; height: 1px;
    background: linear-gradient(90deg, transparent, var(--gold-soft), transparent);
  }
  .gold-rule.upper { left: 120px; top: 214px; width: 350px; }
  .gold-rule.lower { left: 120px; top: 556px; width: 320px; }
  .save-band {
    position: absolute; left: 0; top: 494px; width: 680px; height: 118px;
    background: linear-gradient(90deg, var(--band) 70%, transparent);
  }
  .gig-list { position: absolute; left: 0; top: 0; list-style: none; }
  .gig {
    position: absolute; left: 0; width: 800px; height: 24px;
    font-size: 19px; line-height: 24px; white-space: nowrap;
  }
  .gig span { position: absolute; top: 0; }
  .gig .date { left: 55px; color: var(--date-red); }
  .gig .sep { color: var(--gold-soft); }
  .gig .sep.first { left: 149px; }
  .gig .sep.second { left: 438px; }
  .gig .venue { left: 180px; color: var(--gold); }
  .gig .place { left: 467px; color: var(--text-light); }
  .social {
    position: absolute; left: 54px; top: 614px; height: 22px;
    display: flex; align-items: center; gap: 9px;
  }
  .social .dot { width: 18px; height: 18px; border-radius: 50%; background: var(--social-dot); }
  .social .handle {
    font-family: "Roboto Slab", Georgia, serif; font-size: 17px;
    letter-spacing: 7px; color: var(--text-light);
  }
</style>
</head>
<body>
<main class="poster">
  <div class="photo-area" role="img" aria-label="Photo of the DJ performing at turntables, tinted electric blue"></div>

  <h1 class="brand-name">QUIVER</h1>

  <h2 class="section-title upcoming">UPCOMING DATES</h2>
  <div class="gold-rule upper"></div>

  <div class="save-band"></div>

  <ul class="gig-list">
    <li class="gig" style="top:238px"><span class="date">3/26/18</span><span class="sep first">-</span><span class="venue">Velvet Grotto</span><span class="sep second">-</span><span class="place">(Las Vegas, NV)</span></li>
    <li class="gig" style="top:275px"><span class="date">4/1/18</span><span class="sep first">-</span><span class="venue">Lantern Hall</span><span class="sep second">-</span><span class="place">2847 M St (Sac, CA)</span></li>
    <li class="gig" style="top:311px"><span class="date">4/8/18</span><span class="sep first">-</span><span class="venue">Blue Heron</span><span class="sep second">-</span><span class="place">(Sac, CA)</span></li>
    <li class="gig" style="top:348px"><span class="date">5/5/18</span><span class="sep first">-</span><span class="venue">Open Lanes @ Silver Otter</span><span class="sep second">-</span><span class="place">(Sac, CA)</span></li>
    <li class="gig" style="top:384px"><span class="date">5/10/18</span><span class="sep first">-</span><span class="venue">Dunmore Fine Gallery</span><span class="sep second">-</span><span class="place">(Sac, CA)</span></li>
    <li class="gig" style="top:420px"><span class="date">5/11/18</span><span class="sep first">-</span><span class="venue">Bas Rive @ Cafe du Pont</span><span class="sep second">-</span><span class="place">(Sac, CA)</span></li>
    <li class="gig" style="top:456px"><span class="date">5/27/18</span><span class="sep first">-</span><span class="venue">Sunloft LBW @ Vox</span><span class="sep second">-</span><span class="place">(Sac, CA)</span></li>
    <li class="gig" style="top:571px"><span class="date">9/21/18</span><span class="sep first">-</span><span class="venue">Moonweaver Festival</span><span class="sep second">-</span><span class="place">(Puerto Nuevo, MX)</span></li>
  </ul>

  <h2 class="section-title save">SAVE THE DATE</h2>
  <div class="gold-rule lower"></div>

  <div class="social">
    <span class="dot"></span>
    <span class="handle">FANLOOP.NET/QUIVER530</span>
  </div>
</main>
</body>
</html>
```